Brightpath Orthodontics business card design

Need a business card design that reflects our re-branding (orthodontic office - braces) and a new partnership with a pediatric dental office. We would like to include "for adults and children" on the card as well so adults know they are welcome to get their braces here as well. Office design is modern and would like business card to reflect a modern type look. Here's the text we would like to be included on the card:

Darren Holloway, DDS, MSD
5214 West Maple Avenue, Suite 204
Ridgeview, NM 76099
817-555-0143
www.brightpathortho.example
info@brightpathortho.example
Updates

Can we add the following to the existing designs? Darren Holloway, DDS, MSD 5214 West Maple Avenue, Suite 204 Ridgeview, NM 76099 817-555-0143

Does anyone have any more vertical designs available? Thanks!

Industry/Entity Type

Dental

```html
<!DOCTYPE html>
<html lang="en">
<head>
<meta charset="utf-8">
<title>Brightpath Orthodontics – Business Card</title>
<link rel="stylesheet" href="https://fonts.googleapis.com/css2?family=Arimo:wght@400;700&family=Montserrat:wght@400&display=swap">
<style>
  :root {
    --backdrop: #2e2e2e;
    --card: #ffffff;
    --ink: #1c1c1c;
    --name-blue: #1f4f9a;
    --accent-yellow: #e3d21a;
    --accent-blue: #1574b8;
    --accent-magenta: #d1167d;
    --accent-green: #6ca534;
    --accent-orange: #e07c1c;
    --accent-black: #111111;
    --divider: #333333;
  }
  * { margin: 0; padding: 0; box-sizing: border-box; }
  html, body { width: 1200px; height: 1116px; overflow: hidden; }
  body {
    background: var(--backdrop);
    display: flex; align-items: center; justify-content: center;
    font-family: "Arimo", Arial, sans-serif;
    color: var(--ink);
  }
  .business-card {
    position: relative;
    width: 1050px; height: 600px;
    background: var(--card);
    border-radius: 4px;
    overflow: hidden;
    box-shadow: 0 20px 50px rgba(0,0,0,.5);
  }
  .brand {
    position: absolute; top: 78px; left: 0; width: 100%;
    text-align: center;
  }
  .brand-name {
    display: inline-flex; align-items: center; gap: 18px;
    font-weight: 700; font-size: 54px; color: var(--ink);
    letter-spacing: -0.5px;
  }
  .brand-mark {
    width: 46px; height: 46px; border-radius: 50%;
    background: var(--accent-blue);
    flex: none;
  }
  .brand-tagline {
    margin-top: 14px;
    font-family: "Montserrat", Arial, sans-serif;
    font-size: 21px; letter-spacing: 4px; color: #333;
  }
  .doctor {
    position: absolute; left: 90px; top: 372px; width: 350px;
    text-align: right;
  }
  .doctor-name {
    font-size: 31px; color: var(--name-blue); letter-spacing: .5px;
  }
  .doctor-credentials {
    margin-top: 6px;
    font-size: 24px; font-weight: 700;
  }
  .divider {
    position: absolute; left: 478px; top: 292px;
    width: 3px; height: 200px; background: var(--divider);
  }
  .contact-list {
    position: absolute; left: 520px; top: 300px;
    list-style: none;
  }
  .contact-item {
    display: flex; align-items: flex-start; gap: 16px;
    font-size: 22px; line-height: 27px; margin-bottom: 12px;
  }
  .contact-item svg { width: 26px; height: 26px; flex: none; margin-top: 1px; }
  .colour-band {
    position: absolute; left: 0; bottom: 0; width: 100%; height: 16px;
    display: flex;
  }
  .colour-band span { flex: 1; }
</style>
</head>
<body>
  <article class="business-card">
    <header class="brand">
      <div class="brand-name"><span class="brand-mark"></span>Brightpath Orthodontics</div>
      <p class="brand-tagline">FOR ADULTS &amp; CHILDREN</p>
    </header>

    <section class="doctor">
      <p class="doctor-name">DARREN HOLLOWAY</p>
      <p class="doctor-credentials">DDS, MSD</p>
    </section>

    <div class="divider"></div>

    <ul class="contact-list">
      <li class="contact-item">
        <svg viewBox="0 0 26 26" aria-hidden="true"><path fill="var(--accent-blue)" d="M3 9c0-3 5-5 10-5s10 2 10 5v2h-5V8.5c-1.5-.6-3.2-.9-5-.9s-3.5.3-5 .9V11H3zM6 12h14l3 9H3z"/></svg>
        <span>817-555-0143</span>
      </li>
      <li class="contact-item">
        <svg viewBox="0 0 26 26" aria-hidden="true"><rect x="2" y="5" width="22" height="16" rx="1.5" fill="var(--accent-magenta)"/><path d="M3 6l10 8 10-8" fill="none" stroke="#fff" stroke-width="1.8"/></svg>
        <span>www.brightpathortho.example</span>
      </li>
      <li class="contact-item">
        <svg viewBox="0 0 26 26" aria-hidden="true"><g fill="none" stroke="var(--accent-green)" stroke-width="2.6" stroke-linecap="round"><path d="M11 15l-3 3a3.5 3.5 0 0 1-5-5l4-4a3.5 3.5 0 0 1 5 0"/><path d="M15 11l3-3a3.5 3.5 0 0 1 5 5l-4 4a3.5 3.5 0 0 1-5 0"/></g></svg>
        <span>info@brightpathortho.example</span>
      </li>
      <li class="contact-item">
        <svg viewBox="0 0 26 26" aria-hidden="true"><path fill="var(--accent-orange)" d="M13 2a8 8 0 0 1 8 8c0 6-8 14-8 14S5 16 5 10a8 8 0 0 1 8-8z"/><circle cx="13" cy="10" r="3" fill="#fff"/></svg>
        <span>5214 West Maple Avenue, Suite 204<br>Ridgeview, NM 76099</span>
      </li>
    </ul>

    <div class="colour-band" aria-hidden="true">
      <span style="background: var(--accent-yellow)"></span>
      <span style="background: var(--accent-blue)"></span>
      <span style="background: var(--accent-magenta)"></span>
      <span style="background: var(--accent-green)"></span>
      <span style="background: var(--accent-orange)"></span>
      <span style="background: var(--accent-black)"></span>
    </div>
  </article>
</body>
</html>
```